Spanish Student Needs a Cover for his PhD Dissertation

Hi everyone :) So, I'm a Corneal surgeon currently finishing my PhD, with a dissertation focused on the evaluation of quality of life in patients affected by a disease called Keratoconus. Just so you know, Keratoconus is a condition in which the cornea (the frontal part of the way) gets thin and bulgy and it decreases vision. What I did during my PhD was designing a questionnaire for evaluating quality of life in this kind of patients.
I need to design a hard cover for my dissertation, which is 200 sheets long. I like kind of minimalistic and geometric designs but I am totally open to suggestions. What needs to be in the cover is the name of the dissertation "Diseño, desarrollo y validación de una encuesta para evaluar el compromiso visual y emocional subjetivos en pacientes con Queratocono" and my name, "Iñigo Zabaleta". The other thing that needs to go there is the logo of my university (Universidad de Montealto). Aside from that, anything else is up to the designer. It would be important to use the kind of "red" color I am using in the dissertation. I am attaching the frontal page of my dissertation so you know what kind of design and colors I am using.
In the back part, of the cover, there should be this small inscription: "Iñigo Zabaleta, MD, es un Oftalmólogo Subespecialista en Cirugía Refractiva de la Universidad Católica Mirandina (Colombia) y la Universidad de Montealto (España). Actualmente se desempeña como miembro del Departamento de Córnea y Cirugía Refractiva de la Clínica de Oftalmología Los Robles y como director de su propia compañía de emprendimiento médico Silver Heron Surgical". Please leave a space to place my picture; I will have it taken this week so I don't have it right now, you can just leave the blank spot and I will include it later
The size of the pages is standard "letter" size.
Thanks a lot!

Target Market(s)

PhD Scholars

Font styles to use
Serif

Requirements
Must have
• The "red" color I use on my font. It must be formal but "young".
Nice to have
• I like to keep the design clean, kind of "formal with a young" touch so to speak. I really like gray colors, so it would be nice to have broad areas of gray. I love geometrical designs.
I have uploaded a very early version a friend of mine made (it even had a different title); this can be a starting point for you to work on, but I am more than open to suggestions and new ideas.
Should not have
• Please don't use my whole name, Iñigo Zabaleta is fine. I don't like ALL CAPITALS.

```html
<!DOCTYPE html>
<html lang="es">
<head>
<meta charset="utf-8">
<title>Cubierta de tesis doctoral</title>
<link href="https://fonts.googleapis.com/css2?family=Merriweather:wght@700&family=Montserrat:wght@600;700&family=Gilda+Display&display=swap" rel="stylesheet">
<style>
  :root {
    --page: #ffffff;
    --ink-dark: #262626;
    --wine: #8c1d37;
    --crimson: #b01e42;
    --label-red: #a8173a;
    --band-gray: #bfbfbf;
    --white: #ffffff;
  }
  * { margin: 0; padding: 0; box-sizing: border-box; }
  html, body { width: 1200px; height: 831px; overflow: hidden; background: var(--page); }
  .board { position: relative; width: 1200px; height: 831px; }
  .side-label {
    position: absolute; width: 200px; text-align: center;
    font-family: "Gilda Display", serif; font-size: 21px; color: var(--label-red);
  }
  .side-label--front { left: 215px; top: 53px; }
  .side-label--back { left: 789px; top: 60px; }

  .cover {
    position: absolute; top: 120px; width: 474px; height: 613px; overflow: hidden;
    background: var(--ink-dark);
    box-shadow: 12px 12px 6px rgba(0,0,0,0.85);
  }
  .cover--front { left: 72px; }
  .cover--back { left: 642px; }
  .cover-art { position: absolute; inset: 0; width: 100%; height: 100%; }

  .university {
    position: absolute; left: 336px; top: 12px; width: 128px; text-align: center; color: var(--white);
  }
  .university__seal {
    width: 46px; height: 46px; border-radius: 50%; background: var(--white); margin: 0 auto;
  }
  .university__rule { height: 1px; background: rgba(255,255,255,0.6); margin: 6px 4px 5px; }
  .university__name {
    font-family: "Montserrat", sans-serif; font-weight: 700; font-size: 9px; white-space: nowrap;
  }
  .university__school {
    font-family: "Montserrat", sans-serif; font-weight: 700; font-size: 9px; margin-top: 8px;
  }

  .thesis-title {
    position: absolute; left: 27px; top: 62px; width: 320px;
    font-family: "Merriweather", serif; font-weight: 700; font-size: 18.5px;
    line-height: 24.6px; letter-spacing: 1.1px; color: var(--white);
  }
  .author-name {
    position: absolute; left: 22px; top: 571px;
    font-family: "Montserrat", sans-serif; font-weight: 700; font-size: 20px;
    letter-spacing: 2.4px; color: #111111;
  }

  .author-bio {
    position: absolute; left: 92px; top: 36px; width: 290px; text-align: center;
    font-family: "Gilda Display", serif; font-size: 14.2px; line-height: 16.8px; color: var(--white);
  }
  .photo-slot {
    position: absolute; left: 137px; top: 376px; width: 200px; text-align: center;
    font-family: "Gilda Display", serif; font-size: 14.5px; color: var(--white);
  }
</style>
</head>
<body>
<main class="board">
  <p class="side-label side-label--front">Front</p>
  <p class="side-label side-label--back">Back</p>

  <section class="cover cover--front">
    <svg class="cover-art" viewBox="0 0 474 613" aria-hidden="true">
      <defs>
        <radialGradient id="iris-tones" cx="0.55" cy="0.55" r="0.6">
          <stop offset="0" stop-color="#2a1a10"/>
          <stop offset="0.18" stop-color="#b7782a"/>
          <stop offset="0.42" stop-color="#8a5a2a"/>
          <stop offset="0.7" stop-color="#c46a4a"/>
          <stop offset="1" stop-color="#e6d2cf"/>
        </radialGradient>
      </defs>
      <rect x="0" y="441" width="474" height="172" fill="var(--band-gray)"/>
      <path d="M296 0 H474 V190 C400 196 330 110 296 0 Z" fill="var(--wine)"/>
      <path d="M386 176 L474 110 V190 C440 193 410 187 386 176 Z" fill="#a24058"/>
      <circle cx="250" cy="380" r="200" fill="rgba(255,255,255,0.025)"/>
      <rect x="106" y="264" width="102" height="102" fill="rgba(255,255,255,0.14)" transform="rotate(45 157 315)"/>
      <rect x="89" y="383" width="50" height="50" fill="rgba(255,255,255,0.16)" transform="rotate(45 114 408)"/>
      <rect x="140" y="480" width="80" height="80" fill="rgba(255,255,255,0.22)" transform="rotate(45 180 520)"/>
      <g role="img" aria-label="Fotografía en primer plano de un ojo con iris color avellana y pestañas">
        <circle cx="321" cy="387" r="210" fill="url(#iris-tones)"/>
      </g>
      <rect x="268" y="560" width="60" height="60" fill="rgba(255,255,255,0.25)" transform="rotate(45 298 590)"/>
    </svg>

    <div class="university">
      <div class="university__seal"></div>
      <div class="university__rule"></div>
      <p class="university__name">Universidad de Montealto</p>
      <p class="university__school">Escuela de Doctorado</p>
    </div>

    <h1 class="thesis-title">"Diseño, desarrollo y<br>validación de una encuesta<br>para evaluar el compromiso<br>visual y emocional<br>subjetivos en pacientes con<br>Queratocono"</h1>
    <p class="author-name">Iñigo Zabaleta</p>
  </section>

  <section class="cover cover--back">
    <svg class="cover-art" viewBox="0 0 474 613" aria-hidden="true">
      <circle cx="-69" cy="387" r="196" fill="var(--crimson)"/>
      <circle cx="-69" cy="387" r="96" fill="var(--ink-dark)"/>
      <circle cx="544" cy="387" r="196" fill="var(--crimson)"/>
      <circle cx="544" cy="387" r="99" fill="var(--ink-dark)"/>
    </svg>
    <p class="author-bio">"Iñigo Zabaleta, MD, es un Oftalmólogo Subespecialista en Cirugía Refractiva de la Universidad Católica Mirandina (Colombia) y la Universidad de Montealto (España). Actualmente se desempeña como miembro del Departamento de Córnea y Cirugía Refractiva de la Clínica de Oftalmología Los Robles y como director de su propia compañía de emprendimiento médico Silver Heron Surgical"</p>
    <p class="photo-slot">Author Photo here</p>
  </section>
</main>
</body>
</html>
```